New book cover for "Puddles Under Every Pillow" a book of parenting stories that will warm t.*

Need an alternative to the existing book cover. Cover has to be fun and humorous, there are a lot of puns for the back cover like "S'not Bad at All" "Don't Blow Your Chance to Read this Book"<br/><br/>The stories are funny and moving and convey the joys that parenting can bring as well as some of the frustrations. <br/><br/>The final design has to be as a .pdf using the Velmora Books/ Quarrystone Print template for uploading into their system. The template is available for download from the briefing page.

Target Market(s)

Parents and expectant parents

Colors

Designer to choose colors to be used in the design.

Requirements
Must have
• Fun and playful a cover that reflects the homour and inspiration that is in the stories
Nice to have
• Could be a cartoon like cover or one with cute children

```html
<!DOCTYPE html>
<html lang="en">
<head>
<meta charset="utf-8">
<title>Puddles Under Every Pillow — Book Cover</title>
<link href="https://fonts.googleapis.com/css2?family=Kaushan+Script&family=Roboto+Slab:wght@600;700&display=swap" rel="stylesheet">
<style>
  :root {
    --page-bg: #e4e4e4;
    --cover-navy: #13246b;
    --cover-deep: #0c1a52;
    --title-white: #ffffff;
    --title-edge: #1f7fd4;
    --author-yellow: #f4ec12;
    --author-ink: #13246b;
    --tagline-yellow: #f2e611;
    --photo-pink: #d2578c;
    --photo-blue: #3a5fb8;
    --photo-skin: #e7b9a7;
    --photo-hair: #d9b78a;
  }
  * { margin: 0; padding: 0; box-sizing: border-box; }
  html, body {
    width: 1183px;
    height: 1200px;
    overflow: hidden;
    background: var(--page-bg);
  }
  .book-cover {
    position: absolute;
    left: 214px;
    top: 40px;
    width: 754px;
    height: 1120px;
    background: var(--cover-navy);
    overflow: hidden;
  }
  .cover-photo {
    position: absolute;
    left: 0;
    top: 360px;
    width: 100%;
    height: 760px;
    background:
      radial-gradient(ellipse 150px 190px at 52% 44%, var(--photo-skin) 0%, rgba(231,185,167,0.5) 55%, transparent 100%),
      radial-gradient(ellipse 260px 300px at 50% 35%, var(--photo-hair) 0%, rgba(217,183,138,0.35) 60%, transparent 100%),
      radial-gradient(ellipse 240px 160px at 58% 12%, var(--photo-pink) 0%, transparent 100%),
      radial-gradient(ellipse 340px 260px at 50% 85%, var(--photo-blue) 0%, transparent 100%),
      radial-gradient(ellipse 200px 200px at 8% 70%, rgba(210,87,140,0.55) 0%, transparent 100%),
      linear-gradient(180deg, var(--cover-navy) 0%, #1c2f80 30%, #22388d 100%);
  }
  .cover-title {
    position: absolute;
    left: 0;
    top: 62px;
    width: 100%;
    text-align: center;
    font-family: "Kaushan Script", cursive;
    font-weight: 400;
    font-size: 104px;
    line-height: 1.12;
    color: var(--title-white);
    text-shadow: 4px 5px 0 var(--title-edge);
    transform: rotate(-3deg);
  }
  .cover-title .title-line { display: block; }
  .author-tag {
    position: absolute;
    left: 0;
    top: 415px;
    width: 226px;
    height: 122px;
    background: var(--author-yellow);
    display: flex;
    flex-direction: column;
    align-items: flex-end;
    justify-content: center;
    padding-right: 22px;
    font-family: "Roboto Slab", serif;
    font-weight: 600;
    font-size: 40px;
    line-height: 1.1;
    color: var(--author-ink);
  }
  .cover-tagline {
    position: absolute;
    left: 0;
    top: 940px;
    width: 100%;
    text-align: center;
    font-family: "Roboto Slab", serif;
    font-weight: 700;
    font-size: 33px;
    line-height: 1.18;
    color: var(--tagline-yellow);
    text-shadow: 2px 2px 3px rgba(8,14,50,0.85);
  }
</style>
</head>
<body>
  <main class="book-cover">
    <div class="cover-photo" role="img" aria-label="Photo of a young girl with pink-lit blonde hair in a denim jacket, holding a small card with a finger-and-booger icon over her nose"></div>
    <h1 class="cover-title">
      <span class="title-line">Puddles Under</span>
      <span class="title-line">Every Pillow</span>
    </h1>
    <div class="author-tag">
      <span>Martin</span>
      <span>Halverd</span>
    </div>
    <p class="cover-tagline">Parenting stories to warm the<br>cockles of your heart...<br>and wet the tip of your finger</p>
  </main>
</body>
</html>
```